The Verity (wine label)

We are creating a new wine label for our vineyard in Tasmania, Australia.
This wine is dedicated to a very special person and needs to reflect elegance, beauty and longevity. We are looking for a wine label that incorporates the artwork on the attached photo (serpent tattoo).
We are calling the wine "The Verity" and it is a Pinot Noir (red wine). It is a light bodied but elegant wine, which reflects the person that it is named after.
The wine will be a 2024 Vintage Pinot Noir.

```html
<!DOCTYPE html>
<html lang="en">
<head>
<meta charset="UTF-8">
<title>The Verity – Pinot Noir 2024 Label</title>
<link rel="stylesheet" href="https://fonts.googleapis.com/css2?family=Quicksand:wght@300;400&display=swap">
<style>
  :root {
    --page-bg: #f5f5f5;
    --ink-dark: #2b2b2e;
    --ink-soft: #8a8a90;
    --wine-red: #a3272f;
    --band-red: #8f1418;
    --band-light: #c4555c;
  }
  * { margin: 0; padding: 0; box-sizing: border-box; }
  html, body {
    width: 900px;
    height: 1200px;
    overflow: hidden;
    background: var(--page-bg);
  }
  .canvas {
    position: relative;
    width: 900px;
    height: 1200px;
  }
  .label {
    position: absolute;
    left: 61px;
    top: 194px;
    width: 777px;
    height: 812px;
  }
  .label-shape {
    position: absolute;
    inset: 0;
    width: 100%;
    height: 100%;
  }
  .serpent-artwork {
    position: absolute;
    left: 150px;
    top: 66px;
    width: 490px;
    height: 440px;
    border-radius: 48% 48% 40% 40% / 60% 60% 30% 30%;
    background: radial-gradient(ellipse 58% 70% at 52% 72%,
      rgba(43, 43, 46, 0.62) 0%,
      rgba(90, 90, 96, 0.38) 42%,
      rgba(160, 160, 166, 0.14) 72%,
      rgba(200, 200, 204, 0) 100%);
  }
  .brand-name {
    position: absolute;
    left: 0;
    right: 0;
    top: 522px;
    text-align: center;
    font-family: "Quicksand", sans-serif;
    font-weight: 300;
    font-size: 104px;
    line-height: 1;
    letter-spacing: 2px;
    color: var(--ink-dark);
  }
  .varietal {
    position: absolute;
    left: 0;
    right: 0;
    top: 648px;
    text-align: center;
    font-family: "Quicksand", sans-serif;
    font-weight: 400;
    font-size: 64px;
    line-height: 1;
    color: var(--wine-red);
  }
  .vintage {
    position: absolute;
    left: 0;
    right: 0;
    top: 738px;
    text-align: center;
    font-family: "Quicksand", sans-serif;
    font-weight: 400;
    font-size: 36px;
    line-height: 1;
    letter-spacing: 2px;
    color: var(--wine-red);
  }
</style>
</head>
<body>
<main class="canvas">
  <section class="label">
    <svg class="label-shape" viewBox="0 0 598 625" preserveAspectRatio="none" aria-hidden="true">
      <defs>
        <linearGradient id="paper" x1="0" y1="0" x2="1" y2="0">
          <stop offset="0" stop-color="#eeeeee"/>
          <stop offset="0.25" stop-color="#f8f8f8"/>
          <stop offset="1" stop-color="#d2d2d2"/>
        </linearGradient>
        <linearGradient id="band" x1="0" y1="0" x2="1" y2="0">
          <stop offset="0" stop-color="#8f1418"/>
          <stop offset="0.15" stop-color="#c4555c"/>
          <stop offset="0.55" stop-color="#8f1418"/>
          <stop offset="1" stop-color="#c4555c"/>
        </linearGradient>
      </defs>
      <path class="label-band" fill="url(#band)"
        d="M0 600 H330 C390 600 420 580 452 546 C480 580 505 596 540 596 L598 590 V602 L540 608 C505 608 478 594 452 562 C420 596 390 612 330 612 H0 Z"/>
      <path class="label-paper" fill="url(#paper)"
        d="M0 0 H598 V590 L540 596 C505 596 480 580 452 546 C420 580 390 600 330 600 H0 Z"/>
    </svg>
    <div class="serpent-artwork" role="img" aria-label="Ink wash artwork of a coiled serpent tattoo rising from a spread of black watercolour splashes"></div>
    <h1 class="brand-name">the verity</h1>
    <p class="varietal">Pinot Noir</p>
    <p class="vintage">2024</p>
  </section>
</main>
</body>
</html>
```